Buch-/eBook-Cover für ein jährlichen Referenzbuchs der Industrie
Zielgruppe
verlag-mentoria ist ein Fachverlag mit Fokus auf Industrie und Technologie. Seit über 30 Jahren entwickeln wir Medienangebote für Technologiemärkte – immer mit dem Ziel, komplexe Inhalte verständlich und ansprechend aufzubereiten.
Unsere Arbeit basiert auf einer echten Begeisterung für Technik. Mit unseren Marken bauen wir Brücken zwischen Anbietern und Anwendern – in Print, digital und auf Events.
Wir veröffentlichen Magazine, organisieren Veranstaltungen und entwickeln für Kunden individuelle Kommunikationskampagnen. Unsere Plattformen sind in ihren Zielbranchen fest etabliert und genießen ein hohes Maß an Vertrauen.
Bei dem ausgeschriebenen Projekt handelt es sich um unser WERKBLICK.next LUMIRANO – Das Referenzbuch der Industrie, welches jährlich erscheint. LUMIRANO ist aus dem polynesischen Sprachraum und steht für Freiraum.
WERKBLICK.next LUMIRANO ist ein Referenzbuch, das den Namen verdient: unkonventionell, hochrelevant, emotional, motivierend. Bewusst umgesetzt als hochwertige Print-Referenzpublikation!
Wandel bestimmt unsere Zeit und verändert unsere Gesellschaft, unsere Unternehmen, uns alle.
Im Wandel liegt Freiraum zur Gestaltung. Gesellschaftlicher Wandel, Technologie-Wandel, Klimawandel, Wertewandel, Führungswandel oder Organisationswandel sind nur einige Beispiele. Wer dabei den Wandel in engen Bahnen denkt, verschenkt Potential. Veränderung braucht Freiraum für neue Ideen und Perspektiven sowie Persönlichkeiten, die diesen nutzen wollen.
Unsere Leserzielgruppe – Vorwärtsdenker und Zukunftsmacher:
Strategische & technische Entscheider in der Industrie: Inhaber, Vorstand, Geschäftsführer, Betriebs- & Werksleiter, Bereichs-, Gruppen-, Abteilungs- und Projektleiter
Redaktionelles Konzept:
Wer gestaltet die Zukunft der Industrie und ihrer Branchen? Und wie?
Wir geben Personen aus der Industrie den Freiraum, ihre P..
Aufgabenstellung
1.) Kurzzusammenfassung der Ausschreibung
Die 6. Ausgabe des jährlichen Referenzbuchs der Industrie, WERKBLICK.next LUMIRANO 2026, erscheint im Oktober 2025. Für das Cover sucht verlag-mentoria neue Vorschläge, die nicht automatisch eine Fortsetzung der vorherigen Titel sind.
2.) Gestalterische & Inhaltliche Anforderungen
• Format: 195x250 mm + 3 mm Anschnitt
• Rücken: ca. 1,3 cm (Stand letzte Publikation 2024)
• Auflösung: Druckqualität, mind. 300 dpi
• Inhaltliche Elemente:
- Cover
LUMIRANO 2026 Schriftzug (Orientierung egal)
{polynesisch: Freiraum}
Untersatz: Das Referenzbuch der Industrie. Für Vorwärtsdenker und Zukunftsmacher.
part of WERKBLICK.next Logo-Balken am unteren Rand (siehe Beispiel-Cover LUMIRANO 2025)
3 Statements (je 100-150 Zeichen mit Leerzeichen), zu verwendende Schrift: Helvetica Neue LT Std
Folgende Statements dienen als Beispiel und müssen im Nachgang noch angepasst werden
ERFOLG DURCH FLEXIBILITÄT: IT-ARCHITEKTUREN UND KI TRANSFORMIEREN UNTERNEHMEN GRUNDLEGEND!
PRODUKTIONSFOOTPRINT DEUTSCHER MITTELSTAND 2030+: REGIONAL, 100 % AUTOMATISIERT, KLIMANEUTRAL!
UNTERNEHMEN, DIE FLEXIBEL UND ADAPTIV SIND, KÖNNEN CHANCEN NUTZEN UND INNOVATIONSFÜHRER BLEIBEN.
- Rücken:
LUMIRANO
Jahreszahl: 2026
Zu verwendende Schrift: Helvetica Neue LT Std
WICHTIG: Die Farbe Orange (0/80/100/0) soll als Wiedererkennung in die Gestaltungen eingebunden werden. Wir geben die Cover der vergangenen Jahre als Beispiel und Orientierung mit, möchten aber abgesehen von der Farbe bewusst in eine neue Richtung gehen. Bei der Orientierung und Platzierung der Schriftzüge gibt es daher keine Vorgaben. Zu den Beispiel-Cover LUMIRANO: https://www.werkblick-verlag.example/de/Lumirano/e-paper
Das Design darf nicht zu überladen sein.

```html
<!DOCTYPE html>
<html lang="de">
<head>
<meta charset="utf-8">
<title>WERKBLICK.next LUMIRANO 2026 – Cover und Rücken</title>
<link rel="stylesheet" href="https://fonts.googleapis.com/css2?family=Anton&family=Arimo:wght@400;700&family=Bodoni+Moda:wght@400&display=swap">
<style>
  :root {
    --orange: #e8501a;
    --ink: #0b0b0b;
    --paper: #ffffff;
    --button-light: #f7a37a;
    --button-dark: #d9430f;
  }
  * { margin: 0; padding: 0; box-sizing: border-box; }
  html, body {
    width: 1200px; height: 720px; overflow: hidden;
    background: var(--paper);
  }
  .stage { position: relative; width: 1200px; height: 720px; }

  /* Buchrücken */
  .spine {
    position: absolute; left: 309px; top: 60px;
    width: 50px; height: 600px;
    background: var(--orange);
    color: var(--paper);
  }
  .spine-line {
    position: absolute; left: 25px;
    font-family: "Arimo", Helvetica, Arial, sans-serif;
    font-size: 8px; white-space: nowrap;
    transform-origin: 0 0;
  }
  .spine-tagline { top: 198px; transform: rotate(-90deg) translateY(-4px); }
  .spine-subtitle { top: 557px; transform: rotate(-90deg) translateY(-4px); font-size: 8.5px; }
  .spine-title {
    position: absolute; left: 0; top: 222px; width: 50px;
    text-align: center;
    font-family: "Anton", "Arial Narrow", sans-serif;
    font-size: 34px; line-height: 38px;
    color: var(--ink);
    transform: scaleX(0.82);
  }
  .spine-year {
    position: absolute; left: 0; bottom: 14px; width: 50px;
    text-align: center;
    font-family: "Bodoni Moda", Didot, serif;
    font-size: 16px;
  }

  /* Vorderseite */
  .cover {
    position: absolute; left: 425px; top: 60px;
    width: 466px; height: 600px;
    background: var(--orange);
    color: var(--paper);
    overflow: hidden;
  }
  .cover-head {
    position: absolute; left: 18px; top: 10px;
    display: flex; align-items: center; gap: 10px;
  }
  .cover-year {
    font-family: "Bodoni Moda", Didot, serif;
    font-size: 24px; line-height: 1;
  }
  .cover-subtitle {
    font-family: "Arimo", Helvetica, Arial, sans-serif;
    font-size: 8.5px; line-height: 1.25;
  }
  .emblem { position: absolute; left: 0; top: 0; width: 466px; height: 600px; }
  .emblem-letter {
    font-family: "Anton", "Arial Narrow", sans-serif;
    font-size: 138px;
    fill: var(--ink);
  }
  .translation {
    font-family: "Arimo", Helvetica, Arial, sans-serif;
    font-weight: 700; font-size: 9.5px;
    fill: var(--paper);
  }
  .statements {
    position: absolute; left: 23px; top: 530px; width: 422px;
    font-family: "Arimo", Helvetica, Arial, sans-serif;
    font-size: 7.2px; line-height: 14.5px;
    text-transform: uppercase;
  }
  .statement { text-align: justify; text-align-last: justify; }
  .imprint {
    position: absolute; right: 21px; bottom: 6px;
    display: flex; align-items: baseline; gap: 4px;
  }
  .imprint-label { font-family: "Arimo", Helvetica, Arial, sans-serif; font-size: 5.5px; }
  .imprint-brand {
    font-family: "Anton", "Arial Narrow", sans-serif;
    font-size: 13px; letter-spacing: 0.2px;
  }
</style>
</head>
<body>
<main class="stage">

  <section class="spine" aria-label="Buchrücken">
    <p class="spine-line spine-tagline">Für Vorwärtsdenker und Zukunftsmacher</p>
    <h2 class="spine-title">LU<br>MI<br>RA<br>NO</h2>
    <p class="spine-line spine-subtitle">Das Referenzbuch der Industrie.</p>
    <p class="spine-year">2026</p>
  </section>

  <section class="cover" aria-label="Vorderseite">
    <header class="cover-head">
      <span class="cover-year">2026</span>
      <p class="cover-subtitle">Das Referenzbuch der Industrie.<br>Für Vorwärtsdenker und Zukunftsmacher</p>
    </header>

    <svg class="emblem" viewBox="0 0 466 600" aria-label="LUMIRANO – Buchstaben strahlenförmig um einen Vorspul-Knopf">
      <defs>
        <radialGradient id="button-glow" cx="42%" cy="40%" r="65%">
          <stop offset="0" stop-color="var(--button-light)"/>
          <stop offset="0.55" stop-color="var(--orange)"/>
          <stop offset="1" stop-color="var(--button-dark)"/>
        </radialGradient>
      </defs>
      <g transform="translate(235 272)">
        <circle r="90" fill="url(#button-glow)" role="img" aria-label="Glänzender orangefarbener Knopf mit Vorspul-Symbol"/>
        <g class="emblem-word">
          <text class="emblem-letter" text-anchor="middle" transform="rotate(-16) translate(0 -96) scale(0.82 1)">L</text>
          <text class="emblem-letter" text-anchor="middle" transform="rotate(27) translate(0 -96) scale(0.82 1)">U</text>
          <text class="emblem-letter" text-anchor="middle" transform="rotate(70) translate(0 -96) scale(0.82 1)">M</text>
          <text class="emblem-letter" text-anchor="middle" transform="rotate(113) translate(0 -96) scale(0.82 1)">I</text>
          <text class="emblem-letter" text-anchor="middle" transform="rotate(156) translate(0 -96) scale(0.82 1)">R</text>
          <text class="emblem-letter" text-anchor="middle" transform="rotate(199) translate(0 -96) scale(0.82 1)">A</text>
          <text class="emblem-letter" text-anchor="middle" transform="rotate(242) translate(0 -96) scale(0.82 1)">N</text>
          <text class="emblem-letter" text-anchor="middle" transform="rotate(285) translate(0 -96) scale(0.82 1)">O</text>
        </g>
      </g>
      <text class="translation" transform="translate(82 114) rotate(46)">{polinesisch - Freiraum}</text>
    </svg>

    <div class="statements">
      <p class="statement">Erfolg durch Flexibilität: IT-Architekturen und KI transformieren Unternehmen grundlegend!</p>
      <p class="statement">Produktionsfootprint deutscher Mittelstand 2030+: regional, 100 % automatisiert, klimaneutral!</p>
      <p class="statement">Unternehmen, die flexibel und adaptiv sind, können Chancen nutzen und Innovationsführer bleiben.</p>
    </div>

    <footer class="imprint">
      <span class="imprint-label">part of</span>
      <span class="imprint-brand">WERKBLICK.NEXT</span>
    </footer>
  </section>

</main>
</body>
</html>
```